Design Product Packaging For Face Mask Brand

We need packaging designed for a new product, "Harbor Bloom Cover" a made in canada multi layer poly cotton reusable non-medical face mask for all people. The mask ties in the back behind the head.

Preference is a 4x6' flat polybag or 5x7" resealable stand up bag.

We would like to see bold easy to read colour block designs that use the colour pink. The final design should communicate a simple, high fashion, bold fun quality product.

IMG-9732 and 9733 are of the actual product.
Img_9695 and 9786 are our logos.
Vintageladyshoppinggreenmask is an image on our website.
2020-04_VK is the style of image we would like to have on the front of the packaging.
Maskonworldoff is an example of fun cute wording.

Please leave space for upc on the back of the package aswell. Open to your creativity in terms of design but colors must stay the same as brand.

Thank you all for you time and submissions.

Harbor Bloom Cover xoxo

Target Market(s)

Canada/USA civilians, non-health workers

Industry/Entity Type

Fashion

Font styles to use
Sans Serif

Colors
ffffff
feeeee
f9d9e8
eea4c8
e667a6
e34298
86cfc6
33b8a4
87cfc6

Requirements
Must have
• our logo, brand colors, upc on back
Nice to have
• Bold Font
Should not have
• Hard to read handwriting

```html
<!DOCTYPE html>
<html lang="en">
<head>
<meta charset="utf-8">
<title>Harbor Bloom Cover – Packaging Front</title>
<link rel="stylesheet" href="https://fonts.googleapis.com/css2?family=Roboto+Condensed:wght@700&family=Arimo:wght@700&display=swap">
<style>
  :root {
    --teal-band: #89c5bd;
    --teal-text: #2fa899;
    --blush: #f7ebf1;
    --rose: #dc888a;
    --white: #ffffff;
    --mask-tint: #f3c9dd;
  }
  html, body {
    margin: 0;
    padding: 0;
    width: 857px;
    height: 1200px;
    overflow: hidden;
  }
  .package {
    position: relative;
    width: 857px;
    height: 1200px;
    background: var(--blush);
    box-sizing: border-box;
    border: 1px solid var(--teal-band);
    overflow: hidden;
  }
  .color-band {
    position: absolute;
    left: 0;
    top: 0;
    width: 210px;
    height: 100%;
    background: var(--teal-band);
  }
  .tagline {
    position: absolute;
    left: 70px;
    top: 100px;
    margin: 0;
    font-family: "Roboto Condensed", "Arial Narrow", sans-serif;
    font-weight: 700;
    font-size: 38px;
    letter-spacing: -0.5px;
    white-space: nowrap;
  }
  .tagline .on { color: var(--white); }
  .tagline .off { color: var(--rose); }

  .brand-seal {
    position: absolute;
    left: 568px;
    top: -36px;
    width: 230px;
    height: 230px;
    border-radius: 50%;
    background: var(--white);
    display: flex;
    align-items: center;
    justify-content: center;
    padding-top: 82px;
    box-sizing: border-box;
  }
  .brand-seal__name {
    font-family: "Roboto Condensed", "Arial Narrow", sans-serif;
    font-weight: 700;
    font-size: 19px;
    color: var(--rose);
    text-transform: uppercase;
    white-space: nowrap;
  }

  .product-illustration {
    position: absolute;
    left: 194px;
    top: 646px;
    width: 276px;
    height: 208px;
    border-radius: 40px;
    background: linear-gradient(160deg, var(--white) 0%, var(--mask-tint) 100%);
    z-index: 1;
  }

  .hero-badge {
    position: absolute;
    left: 56px;
    top: 500px;
    width: 300px;
    height: 300px;
    border-radius: 50%;
    background: var(--rose);
    display: flex;
    align-items: center;
    justify-content: center;
    z-index: 2;
  }
  .hero-badge__name {
    margin: 0;
    font-family: "Roboto Condensed", "Arial Narrow", sans-serif;
    font-weight: 700;
    font-size: 62px;
    line-height: 60px;
    color: var(--white);
    text-align: center;
    text-transform: uppercase;
    letter-spacing: -1px;
  }

  .features {
    position: absolute;
    left: 235px;
    top: 892px;
    margin: 0;
    padding: 0;
    list-style: none;
    font-family: "Arimo", "Helvetica", sans-serif;
    font-weight: 700;
    font-size: 36px;
    line-height: 42.6px;
    color: var(--teal-text);
  }
</style>
</head>
<body>
  <main class="package">
    <div class="color-band"></div>

    <h2 class="tagline"><span class="on">Mask on.</span> <span class="off">Connection off!</span></h2>

    <div class="brand-seal">
      <span class="brand-seal__name">Harbor Bloom Cover</span>
    </div>

    <div class="product-illustration" role="img" aria-label="Illustration of a white fabric face mask outlined in magenta"></div>

    <div class="hero-badge">
      <h1 class="hero-badge__name">Harbor<br>Bloom<br>Cover</h1>
    </div>

    <ul class="features">
      <li>Multi layer</li>
      <li>Poly cotton</li>
      <li>Reusable</li>
      <li>Non-medical</li>
      <li>Face mask</li>
    </ul>
  </main>
</body>
</html>
```